2024 Kestrel 2400 Remodeler Truck wrap.

We are a siding/window/roofing/painting company. see our website here: www.tobinsarchway.com.
I'd like a simple, bold, noticeable wrap with our logos and company colors.
Colors should stay simple: Dark Blue, White, Black, Gray.
Tobin's Archway Construction was founded in Chesterfield County, Virginia in 2002 with the goal of providing the highest quality workmanship, and constantly striving to exceed our customer's expectations. Our company performs an array of both residential and commercial building services including roof and siding replacement, installation of new windows, or protecting your home with interior and exterior painting. ​

We are the ONLY home improvement company in Richmond, VA that can offer carpentry, painting, siding and windows. And we completely inspect your home for rotten wood and replace it (if needed) before we do anything else.

Target Market(s)

40-70 year old homeowners

Industry/Entity Type

Construction - remodeling

Colors

Designer to choose colors to be used in the design.

Requirements
Must have
• bold colors and large logos
Should not have
• bright red, bright yellow, people or tools

```html
<!DOCTYPE html>
<html lang="en">
<head>
<meta charset="utf-8">
<title>Tobin's Archway Truck Wrap</title>
<link href="https://fonts.googleapis.com/css2?family=Saira:wght@400;500;600;700&display=swap" rel="stylesheet">
<style>
  :root{
    --bg:#e4e4e6;
    --panel:#f7f8fb;
    --navy:#0f1633;
    --ink:#111318;
    --slate:#7c849e;
    --slate-light:#a9b0c6;
    --pale:#e8ebf3;
  }
  *{margin:0;padding:0;box-sizing:border-box}
  html,body{width:1200px;height:1080px;overflow:hidden;background:var(--bg);font-family:"Saira",sans-serif;color:var(--ink)}
  .wrap-side{position:absolute;left:30px;width:1140px;height:470px;background:var(--panel);border-radius:28px;overflow:hidden}
  .wrap-side--driver{top:30px}
  .wrap-side--passenger{top:580px}
  .band{position:absolute;left:0;top:0;width:1140px;height:470px}
  .phone{position:absolute;display:flex;align-items:center;gap:24px;font-size:52px;font-weight:600;letter-spacing:1px;line-height:1;white-space:nowrap}
  .phone svg{width:46px;height:46px;flex:none}
  .brand{position:absolute;display:flex;flex-direction:column;align-items:flex-start;white-space:nowrap}
  .brand-row{display:flex;align-items:flex-end;gap:16px}
  .brand-mark{width:40px;height:40px;background:var(--navy);margin-bottom:8px}
  .brand-name{font-size:50px;font-weight:700;line-height:.88;color:var(--navy);text-transform:uppercase}
  .brand-services{margin-top:8px;font-size:17px;font-weight:600;letter-spacing:1px;color:var(--navy)}
  .contact{position:absolute;font-size:19px;font-weight:400;color:var(--pale);line-height:1.7;white-space:nowrap}
  .contact-line{display:flex;align-items:center;gap:16px}
  .contact-line svg{width:18px;height:18px;flex:none}
  .social{position:absolute;display:flex;gap:8px}
  .social span{width:28px;height:28px;border-radius:50%;background:var(--navy)}
</style>
</head>
<body>

<section class="wrap-side wrap-side--driver" aria-label="Driver side wrap">
  <svg class="band" viewBox="0 0 1140 470" aria-hidden="true">
    <path fill="var(--slate-light)" d="M60 170 H420 Q450 170 458 200 L480 290 Q488 310 510 310 H900 Q925 310 935 285 L1030 20 H1075 L975 385 Q962 425 925 425 H500 Q465 425 455 390 L420 230 Q415 205 395 205 H60 Z"/>
    <path fill="var(--slate)" opacity=".75" d="M462 335 H965 L955 390 Q945 425 920 425 H500 Q472 425 465 395 Z"/>
    <path fill="none" stroke="var(--navy)" stroke-width="10" d="M60 172 H410 Q440 172 448 200 L490 425"/>
  </svg>
  <div class="phone" style="left:110px;top:42px">
    <svg viewBox="0 0 24 24"><path fill="var(--ink)" d="M6.6 10.8a15 15 0 0 0 6.6 6.6l2.2-2.2a1 1 0 0 1 1-.25 11.4 11.4 0 0 0 3.6.6 1 1 0 0 1 1 1V20a1 1 0 0 1-1 1A17 17 0 0 1 3 4a1 1 0 0 1 1-1h3.5a1 1 0 0 1 1 1c0 1.25.2 2.45.6 3.6a1 1 0 0 1-.25 1z"/><path fill="none" stroke="var(--ink)" stroke-width="1.6" d="M14 3.5a6.5 6.5 0 0 1 6.5 6.5M14 6.8a3.2 3.2 0 0 1 3.2 3.2"/></svg>
    <span>804-555-0178</span>
  </div>
  <div class="brand" style="left:530px;top:165px">
    <div class="brand-row"><span class="brand-mark"></span><span class="brand-name">Tobin's<br>Archway</span></div>
    <div class="brand-services">SIDING | ROOFING | WINDOWS | PAINTING</div>
  </div>
  <div class="contact" style="left:520px;top:342px">
    <div class="contact-line"><svg viewBox="0 0 24 24"><path fill="var(--pale)" d="M12 2a7 7 0 0 0-7 7c0 5 7 13 7 13s7-8 7-13a7 7 0 0 0-7-7zm0 9.5A2.5 2.5 0 1 1 12 6.5a2.5 2.5 0 0 1 0 5z"/></svg>1450 Millbrook Rd. Henrico, VA 23200</div>
    <div class="contact-line"><svg viewBox="0 0 24 24"><circle cx="12" cy="12" r="9" fill="none" stroke="var(--pale)" stroke-width="2"/><path fill="none" stroke="var(--pale)" stroke-width="1.6" d="M3 12h18M12 3c3 3 3 15 0 18M12 3c-3 3-3 15 0 18"/></svg>www.tobinsarchway.com</div>
  </div>
  <div class="social" style="left:1028px;top:196px"><span></span><span></span><span></span></div>
</section>

<section class="wrap-side wrap-side--passenger" aria-label="Passenger side wrap">
  <svg class="band" viewBox="0 0 1140 470" aria-hidden="true">
    <g transform="translate(1140 0) scale(-1 1)">
      <path fill="var(--slate-light)" d="M60 170 H420 Q450 170 458 200 L480 290 Q488 310 510 310 H900 Q925 310 935 285 L1030 20 H1075 L975 385 Q962 425 925 425 H500 Q465 425 455 390 L420 230 Q415 205 395 205 H60 Z"/>
      <path fill="var(--slate)" opacity=".75" d="M462 335 H965 L955 390 Q945 425 920 425 H500 Q472 425 465 395 Z"/>
      <path fill="none" stroke="var(--navy)" stroke-width="10" d="M60 172 H410 Q440 172 448 200 L490 425"/>
    </g>
  </svg>
  <div class="social" style="left:14px;top:196px"><span></span><span></span><span></span></div>
  <div class="brand" style="left:240px;top:165px">
    <div class="brand-row"><span class="brand-mark"></span><span class="brand-name">Tobin's<br>Archway</span></div>
    <div class="brand-services">SIDING | ROOFING | WINDOWS | PAINTING</div>
  </div>
  <div class="contact" style="left:232px;top:342px">
    <div class="contact-line"><svg viewBox="0 0 24 24"><path fill="var(--pale)" d="M12 2a7 7 0 0 0-7 7c0 5 7 13 7 13s7-8 7-13a7 7 0 0 0-7-7zm0 9.5A2.5 2.5 0 1 1 12 6.5a2.5 2.5 0 0 1 0 5z"/></svg>1450 Millbrook Rd. Henrico, VA 23200</div>
    <div class="contact-line"><svg viewBox="0 0 24 24"><circle cx="12" cy="12" r="9" fill="none" stroke="var(--pale)" stroke-width="2"/><path fill="none" stroke="var(--pale)" stroke-width="1.6" d="M3 12h18M12 3c3 3 3 15 0 18M12 3c-3 3-3 15 0 18"/></svg>www.tobinsarchway.com</div>
  </div>
  <div class="phone" style="left:670px;top:42px">
    <svg viewBox="0 0 24 24"><path fill="var(--ink)" d="M6.6 10.8a15 15 0 0 0 6.6 6.6l2.2-2.2a1 1 0 0 1 1-.25 11.4 11.4 0 0 0 3.6.6 1 1 0 0 1 1 1V20a1 1 0 0 1-1 1A17 17 0 0 1 3 4a1 1 0 0 1 1-1h3.5a1 1 0 0 1 1 1c0 1.25.2 2.45.6 3.6a1 1 0 0 1-.25 1z"/><path fill="none" stroke="var(--ink)" stroke-width="1.6" d="M14 3.5a6.5 6.5 0 0 1 6.5 6.5M14 6.8a3.2 3.2 0 0 1 3.2 3.2"/></svg>
    <span>804-555-0178</span>
  </div>
</section>

</body>
</html>
```